Harlune Painting

Need business card design

Target Market(s)

Paint

Industry/Entity Type

Painting

Requirements
Must have
• Brice Halvorn | Superviser
| HarLune Painting
| mobile: (360) 555-0148
| email: Brice@harluneinc.example
| site: www.harluneinc.example
| address: 718 Corliss Rd NE Ste 300, Olympia, WA 98501

```html
<!DOCTYPE html>
<html lang="en">
<head>
<meta charset="utf-8">
<title>Harlune Painting – Business Card</title>
<link rel="stylesheet" href="https://fonts.googleapis.com/css2?family=Crimson+Pro:ital,wght@0,400;0,600;1,400&display=swap">
<style>
  :root {
    --navy: #1c3a85;
    --green: #5fbf21;
    --divider: #4a63a0;
    --paper: #ffffff;
  }
  * { margin: 0; padding: 0; box-sizing: border-box; }
  html, body {
    width: 1200px;
    height: 720px;
    overflow: hidden;
    background: var(--paper);
  }
  .card {
    position: relative;
    width: 1200px;
    height: 720px;
    background: var(--paper);
    font-family: "Crimson Pro", Georgia, serif;
    color: var(--navy);
  }
  .brand {
    position: absolute;
    left: 130px;
    top: 318px;
    width: 420px;
    height: 80px;
    display: flex;
    align-items: center;
    justify-content: center;
    gap: 16px;
  }
  .brand-dot {
    width: 26px;
    height: 26px;
    border-radius: 50%;
    background: var(--green);
    flex: none;
  }
  .brand-name {
    font-weight: 600;
    font-size: 50px;
    color: var(--navy);
    white-space: nowrap;
    line-height: 1;
  }
  .divider {
    position: absolute;
    left: 631px;
    top: 101px;
    width: 2px;
    height: 507px;
    background: var(--divider);
  }
  .contact-person {
    position: absolute;
    left: 664px;
    width: 440px;
    top: 318px;
    text-align: center;
  }
  .person-name {
    font-weight: 600;
    font-size: 50px;
    line-height: 1.1;
    letter-spacing: 0.5px;
  }
  .person-title {
    font-style: italic;
    font-weight: 400;
    font-size: 36px;
    letter-spacing: 1.5px;
    line-height: 1.2;
    margin-top: 2px;
  }
  .contact-list {
    list-style: none;
    margin-top: 28px;
    font-size: 19px;
    font-weight: 400;
    line-height: 1.5;
  }
  .contact-label {
    color: var(--green);
    font-weight: 600;
    margin-right: 6px;
  }
</style>
</head>
<body>
  <main class="card">
    <div class="brand">
      <span class="brand-dot"></span>
      <span class="brand-name">Harlune Painting</span>
    </div>
    <div class="divider"></div>
    <section class="contact-person">
      <h1 class="person-name">Brice Halvorn</h1>
      <p class="person-title">Supervisor</p>
      <ul class="contact-list">
        <li><span class="contact-label">mobile</span>(360) 555-0148</li>
        <li><span class="contact-label">email</span>Brice@harluneinc.example</li>
        <li><span class="contact-label">site</span>www.harluneinc.example</li>
        <li>718 Corliss Rd NE Ste 300, Olympia, WA 98501</li>
      </ul>
    </section>
  </main>
</body>
</html>
```